Business Card for Makeup Artist

I need a business card designed for my makeup and hair artistry business which is primarily events and weddings focused. The card needs to be sleek, simple, stylish and appealing to women. I would prefer a white background but open to suggestions also. I also love the marble background look. I have attached some example pics. It needs to be a double sided card with logo and/or design on one side and contact details in the centre of the card on the other side. NO LOGO ON BACK. Examples attached.

Target Market(s)

Females age 14-55

Industry/Entity Type

Business

Contact Information for Business Card

Nora Vint
Principal Makeup Artist
P: 0413 925 214
E: nora@lumirabeauty.com.au
W: www.lumirabeauty.com.au

Requirements
Should not have
• No yellow, green, red or blue in the design.

```html
<!DOCTYPE html>
<html lang="en">
<head>
<meta charset="utf-8">
<title>Lumira Makeup Artistry – Business Card</title>
<link rel="stylesheet" href="https://fonts.googleapis.com/css2?family=Didact+Gothic&display=swap">
<style>
  :root {
    --canvas: #e6e6e8;
    --card-dark: #1b1b1c;
    --card-light: #ffffff;
    --ink: #1a1a1a;
    --ink-reverse: #f4f4f4;
    --accent: #c94fb5;
    --shadow: 0 10px 28px rgba(0,0,0,0.22);
  }
  html, body {
    margin: 0;
    padding: 0;
    width: 1200px;
    height: 964px;
    overflow: hidden;
    background: var(--canvas);
    font-family: "Didact Gothic", "Century Gothic", sans-serif;
  }
  .stage {
    position: relative;
    width: 1200px;
    height: 964px;
  }
  .card {
    position: absolute;
    left: 320px;
    width: 560px;
    height: 320px;
    box-shadow: var(--shadow);
    box-sizing: border-box;
  }
  .card--front {
    top: 110px;
    background: var(--card-dark);
    display: flex;
    align-items: center;
    justify-content: center;
  }
  .brand {
    text-align: center;
    color: var(--ink-reverse);
  }
  .brand__name {
    display: block;
    font-size: 66px;
    letter-spacing: 4px;
    line-height: 1;
  }
  .brand__tagline {
    display: block;
    margin-top: 12px;
    font-size: 22px;
    letter-spacing: 3px;
    color: var(--ink-reverse);
  }
  .card--back {
    top: 530px;
    background: var(--card-light);
    padding: 70px 0 0 120px;
  }
  .contact__name {
    margin: 0;
    font-size: 30px;
    font-weight: 400;
    color: var(--ink);
    line-height: 1.1;
  }
  .contact__role {
    margin: 2px 0 18px;
    font-size: 18px;
    color: var(--accent);
  }
  .contact__list {
    list-style: none;
    margin: 0;
    padding: 0;
  }
  .contact__item {
    display: flex;
    align-items: center;
    gap: 12px;
    font-size: 18px;
    color: var(--ink);
    margin-bottom: 12px;
  }
  .contact__item svg {
    width: 20px;
    height: 20px;
    flex: none;
  }
</style>
</head>
<body>
<main class="stage">
  <section class="card card--front" aria-label="Card front">
    <div class="brand">
      <span class="brand__name">Lumira</span>
      <span class="brand__tagline">MAKEUP ARTISTRY</span>
    </div>
  </section>

  <section class="card card--back" aria-label="Card back">
    <h1 class="contact__name">Nora Vint</h1>
    <p class="contact__role">Principal Makeup Artist</p>
    <ul class="contact__list">
      <li class="contact__item">
        <svg viewBox="0 0 20 20" aria-hidden="true">
          <path d="M2 7c0-2 3-4 8-4s8 2 8 4v1.5h-4V7H6v1.5H2z" fill="#1a1a1a"/>
          <rect x="4" y="9" width="12" height="8" rx="1" fill="#1a1a1a"/>
          <circle cx="10" cy="13" r="2" fill="#fff"/>
        </svg>
        <span>0413 925 214</span>
      </li>
      <li class="contact__item">
        <svg viewBox="0 0 20 20" aria-hidden="true">
          <rect x="2" y="5" width="16" height="11" fill="#1a1a1a"/>
          <path d="M2.5 5.5 10 11l7.5-5.5" fill="none" stroke="#fff" stroke-width="1.3"/>
        </svg>
        <span>nora@lumirabeauty.com.au</span>
      </li>
      <li class="contact__item">
        <svg viewBox="0 0 20 20" aria-hidden="true" fill="none" stroke="#1a1a1a" stroke-width="1.4">
          <circle cx="10" cy="10" r="7.5"/>
          <ellipse cx="10" cy="10" rx="3.2" ry="7.5"/>
          <path d="M2.5 10h15M4 6h12M4 14h12"/>
        </svg>
        <span>www.lumirabeauty.com.au</span>
      </li>
    </ul>
  </section>
</main>
</body>
</html>
```